Tobelli Kids clothing needs two banners for its website

I have uploaded two images which are already 1767*887 in size, i want two website banners created using each image as a separate banner. I need the banners to be playful and with a lot of colors.
We sell kids clothes such as casual shirts, dresses, polo shirts, jeggings , jeans and cargo pants.
Our products are fashionable but with a unique twist. At the moment we are having 30% sale on all our Jackets.
We have just introduced our spring/summer 2014 collections with unique twist.
We also stock a lot of denim stuff too.
You can use the following messages on the banners: (or you come up with some similar messages)
1.)introducing our look sharp spring summer 2014 collection.
2.)30% Sale on all Jackets.
3.)Checkout our amazing unique styles: dresses, casual shirts, jeggings, pants, jeans ,cargo pants starting from $15
You can use the following messages on the banners:
PLease note: This project is for two separate banners, each image uploaded should be used for separate designs. Thank you
Kids and their parents
Clothing

```html
<!DOCTYPE html>
<html lang="en">
<head>
<meta charset="utf-8">
<title>Light Weight Denim Collections</title>
<link rel="stylesheet" href="https://fonts.googleapis.com/css2?family=Ribeye+Marrow&family=Ribeye&family=Oswald:wght@600&display=swap">
<style>
  :root {
    --canvas: #ffffff;
    --doodle-light: #f7f7f7;
    --doodle-mid: #ececec;
    --headline-red: #e8311c;
    --sale-teal: #1c4f4b;
    --button-top: #f5561f;
    --button-bottom: #d83200;
    --button-text: #ffffff;
    --halo: #ffffff;
    --shadow: rgba(0, 0, 0, 0.28);
    --photo-teal: #5f8f8a;
    --photo-blue: #6a8fb0;
  }
  * { margin: 0; padding: 0; box-sizing: border-box; }
  html, body {
    width: 1200px;
    height: 602px;
    overflow: hidden;
    background: var(--canvas);
  }
  .banner {
    position: relative;
    width: 1200px;
    height: 602px;
    overflow: hidden;
    background: var(--canvas);
  }
  .doodle-backdrop {
    position: absolute;
    inset: 0;
    background: radial-gradient(ellipse at 55% 50%, var(--doodle-mid) 0%, var(--doodle-light) 45%, var(--canvas) 80%);
  }
  .headline {
    position: absolute;
    left: 32px;
    width: 660px;
    text-align: center;
    color: var(--headline-red);
    font-family: "Ribeye Marrow", "Ribeye", cursive;
    line-height: 1;
    white-space: nowrap;
    text-shadow:
      -3px -3px 0 var(--halo), 3px -3px 0 var(--halo),
      -3px 3px 0 var(--halo), 3px 3px 0 var(--halo),
      0 -4px 0 var(--halo), 0 4px 0 var(--halo),
      -4px 0 0 var(--halo), 4px 0 0 var(--halo),
      3px 6px 8px var(--shadow);
  }
  .headline--intro { top: 44px; font-size: 63px; }
  .headline--title { top: 120px; font-size: 82px; }
  .headline--collection { top: 208px; font-size: 56px; }

  .offer {
    position: absolute;
    left: 32px;
    width: 660px;
    text-align: center;
    color: var(--sale-teal);
    font-family: "Ribeye", cursive;
    line-height: 1;
    white-space: nowrap;
  }
  .offer--amount { top: 290px; font-size: 104px; letter-spacing: -2px; }
  .offer--amount .offer__word { font-size: 74px; letter-spacing: 0; }
  .offer--detail { top: 404px; font-size: 40px; }

  .buy-button {
    position: absolute;
    left: 171px;
    top: 477px;
    width: 389px;
    height: 74px;
    border-radius: 6px;
    background: linear-gradient(to bottom, var(--button-top), var(--button-bottom));
    box-shadow: 0 14px 14px -6px var(--shadow);
    color: var(--button-text);
    font-family: "Oswald", sans-serif;
    font-weight: 600;
    font-size: 44px;
    line-height: 74px;
    text-align: center;
    text-decoration: none;
    letter-spacing: 1px;
    text-shadow: 1px 2px 2px rgba(0, 0, 0, 0.35);
  }

  .kids-photo {
    position: absolute;
    left: 715px;
    top: 33px;
    width: 410px;
    height: 550px;
    border-radius: 40px;
    background: linear-gradient(90deg, var(--photo-teal) 0%, var(--photo-teal) 48%, var(--photo-blue) 58%, var(--photo-blue) 100%);
    opacity: 0.55;
  }
</style>
</head>
<body>
<main class="banner">
  <div class="doodle-backdrop" role="img" aria-label="Faint hand-drawn school doodles: books, light bulbs, backpacks and science icons"></div>

  <h1 class="headline headline--intro">Checkout our</h1>
  <p class="headline headline--title">Light Weight</p>
  <p class="headline headline--collection">Denim Collections</p>

  <p class="offer offer--amount">30%<span class="offer__word">Sale</span></p>
  <p class="offer offer--detail">on all our Jackets</p>

  <a class="buy-button" href="#">BUY NOW!</a>

  <div class="kids-photo" role="img" aria-label="Photo of a smiling girl in a teal denim dress holding hands with a boy in a blue denim shirt and dark shorts"></div>
</main>
</body>
</html>
```